Venture Backed Startup Company for SaaS Lead Generation ***Guaranteed Payment and Fast Feedback***

***Guaranteed Payment***
***I Give Fast Feedback***

I need a one-page website design for a startup company. We sell lead generation and appointment setting services to B2B SaaS companies.

Looking for a clean, modern, flat, "Saas-style" design. A simple but trustworthy and authoritative color palette is best. Pictures of actual people are very good to use too

Here are some websites I like and the reasons why:

https://www.pellarin.com - simple and intuitive design, very clear, strong CTA, explains the process succinctly, and has pics of people/faces\

https://www.tovemark.com/ - clean and simple, flat design, strong CTA, easy to understand

https://www.quorvel.io/ - simple and clean navigation, easy to understand what to do next

https://brisketfolder.com/ - strong step by step approach, easy to understand the value of the website, clean and sharp design

https://pinwardle.com/ - Great color scheme, clean, easy to read, great font

Target Market(s)

startups, entrepeneur, B2B SaaS

Industry/Entity Type

SaaS

Number of Pages Required

1 page

Font styles to use
Sans Serif

Colors

Designer to choose colors to be used in the design.

Requirements
Must have
• Good graphics, a theme, and pictures of people
Nice to have
• Here are other websites like and the reason why
• https://marqueloft.com/ - Great graphics, clean and flat design, pictures of people, modern design
• https://dunvelio.com/ - Clean, pictures of people, easy to read, good contrast
• https://yarrowpeak.co/ -- Good graphics and great font, easy to read, great color scheme
• http://tillerandvane.com/ - clean design

```html
<!DOCTYPE html>
<html lang="en">
<head>
<meta charset="utf-8">
<title>Lead Generation &amp; Appointment Setting</title>
<link rel="stylesheet" href="https://fonts.googleapis.com/css2?family=Montserrat:wght@400;500;600;700&display=swap">
<style>
:root{
  --blue:#1f63d6;
  --blue-bright:#1a7bff;
  --blue-soft:#eef4ff;
  --ink:#4a4f5c;
  --orange:#ff8a1f;
  --orange-deep:#f46a12;
  --white:#ffffff;
  --line:#e6e9f0;
}
*{margin:0;padding:0;box-sizing:border-box}
html,body{width:1200px;height:2695px;overflow:hidden;background:var(--white)}
body{position:relative;font-family:"Montserrat",sans-serif;color:var(--ink)}
.abs{position:absolute}
.decor{position:absolute;top:0;left:0}
.logo{left:149px;top:42px;font-size:24px;font-weight:700;letter-spacing:4px;color:var(--white)}
.nav{left:0;top:0}
.nav a{position:absolute;top:45px;font-size:13px;font-weight:500;color:var(--blue);text-decoration:none;white-space:nowrap}
.nav a.active{color:var(--orange-deep)}
.nav a.active::after{content:"";position:absolute;left:0;right:0;bottom:-14px;height:2px;background:var(--orange-deep)}
.btn{position:absolute;display:flex;align-items:center;justify-content:center;border-radius:22px;
  background:linear-gradient(90deg,var(--orange),var(--orange-deep));color:var(--white);
  font-size:12px;font-weight:600;text-decoration:none;box-shadow:0 8px 16px rgba(244,106,18,.28)}
.hero-title{left:149px;top:238px;width:540px;font-size:33px;line-height:45px;font-weight:700;color:var(--blue)}
.h2{font-size:25px;font-weight:700;color:var(--blue)}
.body-text{font-size:13px;line-height:24px;color:var(--ink)}
.checks{list-style:none;left:149px;top:809px}
.checks li{position:relative;padding-left:37px;height:36px;line-height:24px;font-size:13px}
.checks li::before{content:"";position:absolute;left:0;top:5px;width:14px;height:14px;border-radius:50%;background:var(--orange)}
.checks li::after{content:"";position:absolute;left:4px;top:8px;width:6px;height:3px;border-left:2px solid #fff;border-bottom:2px solid #fff;transform:rotate(-45deg)}
.partners-label{left:756px;top:646px;width:162px;text-align:center;font-size:13px;font-weight:700;letter-spacing:2.5px;color:var(--blue)}
.partner{position:absolute;left:756px;width:162px;height:60px;background:var(--white);box-shadow:0 3px 10px rgba(30,60,120,.14);display:flex;align-items:center;justify-content:center}
.partner span{display:block;width:80px;height:20px;border-radius:4px;background:#d9dde5}
.center{left:0;width:1200px;text-align:center}
.feature{position:absolute;top:1330px;width:300px;text-align:center}
.feature .hex{display:block;margin:0 auto}
.feature h3{margin-top:36px;font-size:14.5px;font-weight:600;color:var(--blue)}
.feature p{margin-top:14px;font-size:12.5px;line-height:24px}
.num{position:absolute;left:135px;width:66px;height:66px}
.num b{position:absolute;inset:0;display:flex;align-items:center;justify-content:center;font-size:32px;font-weight:700;color:var(--blue)}
.svc-title{position:absolute;left:221px;font-size:18px;font-weight:600;color:var(--blue)}
.svc-text{position:absolute;left:223px;width:410px}
.svc-text p+p{margin-top:22px}
.illo{position:absolute}
</style>
</head>
<body>

<svg class="decor" width="1200" height="2695" viewBox="0 0 1200 2695" aria-hidden="true">
  <defs>
    <linearGradient id="corner" x1="0" y1="0" x2="1" y2="1">
      <stop offset="0" stop-color="#1a86ff"/><stop offset="1" stop-color="#1560e0"/>
    </linearGradient>
  </defs>
  <path d="M0 0 H404 L210 112 Q190 124 165 120 L0 90 Z" fill="url(#corner)"/>
  <path d="M300 0 H480 L360 70 Z" fill="#eef4ff"/>
  <g fill="#eef4ff">
    <path d="M545 170 l40-20 45 20 -40 22z"/>
    <path d="M30 525 l38-18 42 18 -38 20z"/>
    <path d="M0 1020 l40 20 60 30 -60 40 -40-20z"/>
    <path d="M1060 1085 l60-30 80 30 -60 35z"/>
    <path d="M1005 1180 l40-18 45 18 -40 22z"/>
  </g>
</svg>

<div class="abs logo">LOGO</div>

<nav class="nav abs">
  <a class="active" style="left:440px" href="#about">About Us</a>
  <a style="left:550px" href="#features">Features</a>
  <a style="left:652px" href="#services">Services</a>
  <a style="left:754px" href="#testimonials">Testimonials</a>
  <a style="left:884px" href="#pricing">Pricing</a>
</nav>
<a class="btn" href="#signup" style="left:972px;top:35px;width:106px;height:40px">Sign Up</a>

<h1 class="abs hero-title">Lead Generation &amp; Appointment Setting Services for B2B SaaS Companies</h1>
<a class="btn" href="#more" style="left:149px;top:414px;width:136px;height:41px">Learn More</a>

<svg class="illo" style="left:664px;top:150px" width="536" height="520" viewBox="0 0 536 520" role="img" aria-label="Isometric illustration of a laptop with a rocket launching from the screen, charts and clouds">
  <defs>
    <linearGradient id="heroBand" x1="0" y1="0" x2="1" y2="1">
      <stop offset="0" stop-color="#2a8cff"/><stop offset="1" stop-color="#1560e6"/>
    </linearGradient>
  </defs>
  <path d="M10 225 L290 60 L536 200 V510 L260 360 Q230 345 200 350 Z" fill="url(#heroBand)"/>
  <path d="M120 190 L280 100 L440 190 L280 280 Z" fill="#dfeafc" opacity=".9"/>
  <path d="M230 60 L300 20 L360 55 L290 95 Z" fill="#ff8a1f" opacity=".85"/>
</svg>

<h2 class="abs h2" id="about" style="left:149px;top:598px">About Us</h2>
<p class="abs body-text" style="left:149px;top:675px;width:470px">We create modern IT solutions to increase lead generation and provide appointment setting services to B2B SaaS companies. Aliquam posuere augue vitae metu feugiat pellentesque. Pellentesque habiant morbitus tristique senectus et netus et malesuada fames ac turpis egestas.</p>
<ul class="abs checks">
  <li>Find new prospects</li>
  <li>Get full profile information with verified emails</li>
  <li>Use your network to reach more prospects</li>
  <li>Gain access to more accounts through team network</li>
  <li>Enrich your marketing data</li>
  <li>95% email accuracy guarantee</li>
</ul>

<div class="abs partners-label">OUR PARTNERS</div>
<div class="partner" style="top:684px"><span></span></div>
<div class="partner" style="top:754px"><span></span></div>
<div class="partner" style="top:823px"><span></span></div>
<div class="partner" style="top:893px"><span></span></div>
<div class="partner" style="top:961px"><span></span></div>

<h2 class="abs h2 center" id="features" style="top:1151px">Our Key Features</h2>
<p class="abs body-text center" style="top:1198px;font-size:12.5px">Here are the best features that makes us the most<br>powerful, fast and user-friendly platform.</p>

<div class="feature" style="left:128px">
  <svg class="hex" width="110" height="110" viewBox="0 0 110 110" aria-hidden="true">
    <path d="M55 4 L100 30 L100 80 L55 106 L10 80 L10 30 Z" fill="#eef4ff"/>
    <circle cx="48" cy="52" r="11" fill="none" stroke="#1a7bff" stroke-width="2.5"/>
    <circle cx="66" cy="64" r="8" fill="none" stroke="#1a7bff" stroke-width="2.5"/>
    <path d="M34 40 q4-12 18-10 q6-8 16 0 q10 0 8 10" fill="none" stroke="#1a7bff" stroke-width="2.5"/>
  </svg>
  <h3>Cloud Based Services</h3>
  <p>Nam in est quis lectus viverra blandit.<br>Curabitur quam sem, imperdiet nec<br>auctor quis, vehicula non est.</p>
</div>
<div class="feature" style="left:450px">
  <svg class="hex" width="110" height="110" viewBox="0 0 110 110" aria-hidden="true">
    <path d="M55 4 L100 30 L100 80 L55 106 L10 80 L10 30 Z" fill="#eef4ff"/>
    <rect x="36" y="38" width="38" height="36" rx="3" fill="none" stroke="#1a7bff" stroke-width="2.5"/>
    <circle cx="55" cy="56" r="8" fill="none" stroke="#1a7bff" stroke-width="2.5"/>
    <path d="M40 78 v4 M70 78 v4" stroke="#1a7bff" stroke-width="2.5"/>
  </svg>
  <h3>Data Safe Solutions</h3>
  <p>Ut lorem magna, accumsan at tellus sit<br>amet, dignissim vulputate risus. Class<br>aptent taciti sociosqu ad litora torquen.</p>
</div>
<div class="feature" style="left:775px">
  <svg class="hex" width="110" height="110" viewBox="0 0 110 110" aria-hidden="true">
    <path d="M55 4 L100 30 L100 80 L55 106 L10 80 L10 30 Z" fill="#eef4ff"/>
    <rect x="34" y="36" width="30" height="10" fill="#1a7bff"/>
    <rect x="34" y="50" width="30" height="10" fill="#1a7bff"/>
    <rect x="34" y="64" width="30" height="10" fill="#1a7bff"/>
    <path d="M62 50 q2-10 12-8 q8-4 12 4 q6 2 4 8 h-28" fill="none" stroke="#1a7bff" stroke-width="2.5"/>
  </svg>
  <h3>Fast &amp; Reliable Storage</h3>
  <p>Porttitor mollis quam quis aliquam. Fus<br>varius massa vitae mauris vehicula, ac<br>dictum ipsum auctor.</p>
</div>

<h2 class="abs h2 center" id="services" style="top:1737px">Our Services</h2>

<div class="num" style="top:1841px">
  <svg width="66" height="66" viewBox="0 0 66 66" aria-hidden="true"><path d="M33 2 L61 18 L61 48 L33 64 L5 48 L5 18 Z" fill="#eef4ff"/></svg>
  <b>1</b>
</div>
<h3 class="svc-title" style="top:1860px">Lead Generation</h3>
<div class="svc-text body-text" style="top:1915px">
  <p>Praesent et tellus leo. Donec porta eu eros in tempor. Praesent condimentum, est in egestas iaculis, libero mauris consectetur leo, sed sollicitudin odio metus in arcu. Vestibulum fringilla.</p>
  <p>Etiam vestibulum, leo sit amet eleifend porta, urna justo est maximus orci, non ullamcorper ipsum quam eget lacus. Sed commodo velit non nulla porttitor placerat porta. Vestibulum neque nisl, pretium nec arcu sit amet.</p>
</div>
<a class="btn" href="#lead" style="left:223px;top:2142px;width:135px;height:41px">Learn More</a>
<svg class="illo" style="left:718px;top:1859px" width="370" height="315" viewBox="0 0 370 315" role="img" aria-label="Isometric illustration of a team working with dashboards, charts and data panels">
  <defs><linearGradient id="svc1" x1="0" y1="0" x2="1" y2="1"><stop offset="0" stop-color="#dce8ff"/><stop offset="1" stop-color="#f4f8ff"/></linearGradient></defs>
  <path d="M20 230 L190 130 L360 230 L190 315 Z" fill="url(#svc1)"/>
  <path d="M120 20 L260 0 L300 200 L160 230 Z" fill="#cfe0ff"/>
</svg>

<div class="num" style="top:2301px">
  <svg width="66" height="66" viewBox="0 0 66 66" aria-hidden="true"><path d="M33 2 L61 18 L61 48 L33 64 L5 48 L5 18 Z" fill="#eef4ff"/></svg>
  <b>2</b>
</div>
<h3 class="svc-title" style="top:2321px;left:224px">Appointment Setting</h3>
<div class="svc-text body-text" style="top:2378px">
  <p>Suspendisse in vestibulum est. Duis blandit, erat at varius erat venenatis, purus nisl pretium libero, quis hendrerit lacus tortor ac nibh. Curabitur at metus aliquam, volutpat orci.</p>
  <p>Morbi suscipit interdum mi, at lobortis erat efficitur a nec. Mauris molestie dignissim lacus, nec tincidunt dui mollis in. Orci varius natoque penatibus et magnis dis parturient montes, nascetur ridiculus mus. Aenean tincidunt nisi quis pulvinar lobortis velit.</p>
</div>
<a class="btn" href="#appointments" style="left:223px;top:2603px;width:135px;height:41px">Learn More</a>
<svg class="illo" style="left:709px;top:2317px" width="388" height="315" viewBox="0 0 388 315" role="img" aria-label="Isometric illustration of a laptop surrounded by analytics charts, graphs and gears">
  <defs><linearGradient id="svc2" x1="0" y1="0" x2="1" y2="1"><stop offset="0" stop-color="#2a7cf0"/><stop offset="1" stop-color="#dbe8ff"/></linearGradient></defs>
  <path d="M20 200 L200 100 L380 200 L200 300 Z" fill="#eef4ff"/>
  <path d="M150 20 L300 0 L330 200 L170 230 Z" fill="url(#svc2)" opacity=".85"/>
  <path d="M200 120 L280 80 L300 180 L220 220 Z" fill="#ff9a3a" opacity=".75"/>
</svg>

</body>
</html>
```